Criação de Papelaria (6 itens) para Automotivo
" Somos uma loja compacta e o nosso diferencial é o bom atendimento personalizado que damos ao cliente, e que a maioria elogia. Compramos, vendemos, trocamos e aceitamos carros consignados. "

```html
<!DOCTYPE html>
<html lang="pt-BR">
<head>
<meta charset="UTF-8">
<title>Safira Veículos — Cartão de Visita</title>
<link rel="stylesheet" href="https://fonts.googleapis.com/css2?family=Montserrat:wght@800&family=Roboto:wght@400;500&display=swap">
<style>
  :root {
    --page-bg: #e9e9e9;
    --orange: #f08a1c;
    --orange-deep: #d96f0c;
    --orange-light: #ffb14a;
    --ink: #1c1c1c;
    --black: #121212;
    --black-soft: #262626;
    --white: #ffffff;
    --mascot-a: #e9e4d8;
    --mascot-b: #c98a3a;
  }
  * { margin: 0; padding: 0; box-sizing: border-box; }
  html, body { width: 1200px; height: 1200px; overflow: hidden; }
  body {
    background: var(--page-bg);
    font-family: "Roboto", Arial, sans-serif;
    display: flex;
    flex-direction: column;
    align-items: center;
    justify-content: center;
    gap: 50px;
  }
  .card {
    width: 900px;
    height: 515px;
    border-radius: 6px;
    position: relative;
    overflow: hidden;
    box-shadow: 0 10px 28px rgba(0,0,0,.18);
  }

  /* Front: contact side */
  .card--front {
    background: linear-gradient(135deg, var(--orange-light) 0%, var(--orange) 45%, var(--orange-deep) 100%);
  }
  .card--front .brand-name {
    position: absolute;
    left: 60px;
    top: 100px;
    font-family: "Montserrat", Arial, sans-serif;
    font-weight: 800;
    font-size: 50px;
    line-height: 1.02;
    color: var(--white);
    text-transform: uppercase;
  }
  .contact-list {
    position: absolute;
    left: 60px;
    top: 260px;
    list-style: none;
    display: flex;
    flex-direction: column;
    gap: 22px;
  }
  .contact-item {
    display: flex;
    align-items: center;
    gap: 16px;
    color: var(--ink);
    font-size: 20px;
    line-height: 1.25;
  }
  .contact-icon {
    width: 36px;
    height: 36px;
    border-radius: 7px;
    background: var(--ink);
    flex: none;
    display: flex;
    align-items: center;
    justify-content: center;
  }
  .mascot-area {
    position: absolute;
    right: 60px;
    top: 50px;
    width: 300px;
    height: 410px;
    border-radius: 48% 48% 40% 40%;
    background: radial-gradient(circle at 45% 35%, var(--mascot-a) 0%, var(--mascot-b) 70%, var(--orange-deep) 100%);
    opacity: .85;
  }

  /* Back: brand side */
  .card--back {
    background: radial-gradient(ellipse at 50% 45%, var(--black-soft) 0%, var(--black) 75%);
    display: flex;
    align-items: center;
    justify-content: center;
  }
  .brand-block {
    display: flex;
    flex-direction: column;
    gap: 16px;
  }
  .card--back .brand-name {
    font-family: "Montserrat", Arial, sans-serif;
    font-weight: 800;
    font-size: 82px;
    line-height: 1.02;
    color: var(--orange);
    text-transform: uppercase;
  }
  .tagline {
    font-family: "Roboto", Arial, sans-serif;
    font-weight: 400;
    font-size: 30px;
    color: var(--white);
    align-self: flex-end;
  }
</style>
</head>
<body>

  <section class="card card--front" aria-label="Frente do cartão">
    <div class="brand-name">Safira<br>Veículos</div>

    <ul class="contact-list">
      <li class="contact-item">
        <span class="contact-icon">
          <svg width="20" height="20" viewBox="0 0 24 24" fill="#ffffff"><path d="M6.6 10.8a15.1 15.1 0 0 0 6.6 6.6l2.2-2.2a1 1 0 0 1 1-.25 11.4 11.4 0 0 0 3.6.57 1 1 0 0 1 1 1V20a1 1 0 0 1-1 1A17 17 0 0 1 3 4a1 1 0 0 1 1-1h3.5a1 1 0 0 1 1 1c0 1.25.2 2.45.57 3.57a1 1 0 0 1-.25 1z"/></svg>
        </span>
        <span>(00) 0000-0000</span>
      </li>
      <li class="contact-item">
        <span class="contact-icon">
          <svg width="20" height="20" viewBox="0 0 24 24" fill="none" stroke="#ffffff" stroke-width="2"><rect x="3" y="5" width="18" height="14" rx="2"/><path d="M3 7l9 6 9-6"/></svg>
        </span>
        <span>contato@exemplo.com.br</span>
      </li>
      <li class="contact-item">
        <span class="contact-icon">
          <svg width="20" height="20" viewBox="0 0 24 24" fill="#ffffff"><path d="M12 2a7 7 0 0 0-7 7c0 5.2 7 13 7 13s7-7.8 7-13a7 7 0 0 0-7-7zm0 9.5A2.5 2.5 0 1 1 12 6.5a2.5 2.5 0 0 1 0 5z"/></svg>
        </span>
        <span>Rua exemplo, 000<br>Cidade - UF, CEP: 00000-000</span>
      </li>
    </ul>

    <div class="mascot-area" role="img" aria-label="Mascote da loja segurando uma chave de carro"></div>
  </section>

  <section class="card card--back" aria-label="Verso do cartão">
    <div class="brand-block">
      <div class="brand-name">Safira<br>Veículos</div>
      <div class="tagline">Sua melhor opção</div>
    </div>
  </section>

</body>
</html>
```